K&T'S Poultry Pail Need a Flyer Design

I am opening a new fast food.... take out only .... fried chicken, fries, drinks etc etc.
I need something to start my advertising and to hand out in the neighborhood and surrounding areas. Introduction
I would also like to offer some sort of coupon on the flyer, example: $5 off a family meal on Friday, Saturday and Sunday only or maybe a special on a specific day. I am open to any ideas in this area. But I need to offer something to bring customers in.

Something special to entice customers to come to my restaurant.

Also the flyer may state: Free Delivery with a minimum of $20 order within 2 mile radius. (or something similar)

I will attach my logo to assist you.

I also like the new style flyers/postcard size approx.: 8.5 x 5.4 Lets see what you can do with this size as well.

Address of restaurant: 847 North Alder Lane, Statesboro, Georgia

Target Market(s)

Fast Food Restaurant: Family Friendly

Industry/Entity Type

Advertising

Requirements
Nice to have
• Some sort of special or Coupon to entice customers to come t my location

```html
<!DOCTYPE html>
<html lang="en">
<head>
<meta charset="utf-8">
<title>K&amp;T'S Poultry Pail – Grand Opening Flyer</title>
<link rel="stylesheet" href="https://fonts.googleapis.com/css2?family=Alfa+Slab+One&family=Roboto+Slab:wght@700;800&display=swap">
<style>
  :root {
    --red: #d3132a;
    --red-deep: #a50d1f;
    --red-soft: #e8534f;
    --yellow: #f7e70e;
    --white: #ffffff;
    --ink: #1c1c1c;
    --food-light: #e9a552;
    --food-dark: #b8621f;
  }
  * { margin: 0; padding: 0; box-sizing: border-box; }
  html, body { width: 763px; height: 1200px; overflow: hidden; background: var(--white); }
  .flyer {
    position: relative;
    width: 763px;
    height: 1200px;
    overflow: hidden;
    background: var(--white);
    font-family: "Alfa Slab One", "Roboto Slab", serif;
    color: var(--red);
  }
  .hero {
    position: absolute;
    left: 0; top: 0;
    width: 763px; height: 560px;
  }
  .hero svg { display: block; width: 100%; height: 100%; }
  .brand {
    position: absolute;
    left: 0; right: 0; top: 250px;
    display: flex;
    justify-content: center;
    align-items: center;
    gap: 16px;
  }
  .brand-dot {
    width: 26px; height: 26px;
    border-radius: 50%;
    background: var(--yellow);
  }
  .brand-name {
    font-family: "Alfa Slab One", serif;
    font-size: 58px;
    line-height: 1;
    color: var(--white);
    letter-spacing: 1px;
  }
  .headline {
    position: absolute;
    left: 0; right: 0;
    text-align: center;
    font-size: 62px;
    line-height: 1;
    letter-spacing: 1px;
    color: var(--red);
  }
  .headline--opening { top: 515px; }
  .headline--takeout { top: 660px; }
  .address-bar {
    position: absolute;
    left: 81px; top: 597px;
    width: 643px; height: 44px;
    background: var(--yellow);
    display: flex;
    align-items: center;
    justify-content: center;
    font-family: "Roboto Slab", serif;
    font-weight: 800;
    font-size: 22px;
    color: var(--red);
    letter-spacing: 0.5px;
  }
  .food-photo {
    position: absolute;
    left: 248px; top: 730px;
    width: 266px; height: 128px;
  }
  .divider {
    position: absolute;
    left: 0; top: 862px;
    width: 763px; height: 6px;
    background: var(--red);
  }
  .coupons {
    position: absolute;
    left: 0; top: 868px;
    width: 763px; height: 332px;
    display: grid;
    grid-template-columns: 1fr 1fr;
    grid-template-rows: 153px 179px;
  }
  .coupon {
    display: flex;
    flex-direction: column;
    align-items: center;
    text-align: center;
    padding-top: 18px;
    border-right: 3px dashed var(--red);
    border-bottom: 3px dashed var(--red);
  }
  .coupon:nth-child(2n) { border-right: none; }
  .coupon--senior { padding-top: 36px; border-bottom: none; }
  .coupon-value {
    font-size: 66px;
    line-height: 1;
    color: var(--red);
  }
  .coupon-terms {
    margin-top: 10px;
    font-family: "Roboto Slab", serif;
    font-weight: 800;
    font-size: 15px;
    line-height: 1.2;
    color: var(--red);
    text-transform: uppercase;
  }
</style>
</head>
<body>
  <main class="flyer">
    <header class="hero">
      <svg viewBox="0 0 763 560" preserveAspectRatio="none" role="img" aria-label="Close-up photo of crispy fried chicken, fries and a biscuit on a red background">
        <defs>
          <linearGradient id="heroTone" x1="0" y1="0" x2="1" y2="1">
            <stop offset="0" stop-color="#c8242c"/>
            <stop offset="0.45" stop-color="#e24a3c"/>
            <stop offset="0.75" stop-color="#d6542e"/>
            <stop offset="1" stop-color="#b51a24"/>
          </linearGradient>
        </defs>
        <rect width="763" height="560" fill="url(#heroTone)"/>
        <path d="M0 470 C 200 500, 480 470, 763 400 L763 560 L0 560 Z" fill="var(--white)"/>
      </svg>
    </header>

    <div class="brand">
      <span class="brand-dot"></span>
      <span class="brand-name">K&amp;T'S Poultry Pail</span>
    </div>

    <h1 class="headline headline--opening">GRAND OPENING</h1>
    <p class="address-bar">847 NORTH ALDER LANE, STATESBORO, GEORGIA</p>
    <h2 class="headline headline--takeout">TAKE OUT ONLY</h2>

    <svg class="food-photo" viewBox="0 0 266 128" role="img" aria-label="Photo of a plate of fried chicken pieces with fries and a biscuit">
      <defs>
        <radialGradient id="foodTone" cx="0.5" cy="0.45" r="0.55">
          <stop offset="0" stop-color="var(--food-light)"/>
          <stop offset="1" stop-color="var(--food-dark)"/>
        </radialGradient>
      </defs>
      <ellipse cx="133" cy="68" rx="128" ry="56" fill="url(#foodTone)"/>
    </svg>

    <div class="divider"></div>

    <section class="coupons">
      <article class="coupon coupon--family">
        <p class="coupon-value">$5 OFF</p>
        <p class="coupon-terms">A family meal<br>Friday only</p>
      </article>
      <article class="coupon coupon--family">
        <p class="coupon-value">$5 OFF</p>
        <p class="coupon-terms">A family meal<br>Friday only</p>
      </article>
      <article class="coupon coupon--senior">
        <p class="coupon-value">10%</p>
        <p class="coupon-terms">Senior citizen discount<br>Wednesdays only</p>
      </article>
      <article class="coupon coupon--senior">
        <p class="coupon-value">10%</p>
        <p class="coupon-terms">Senior citizen discount<br>Wednesdays only</p>
      </article>
    </section>
  </main>
</body>
</html>
```